Quote Cards With KB May 2025 for Instagram

I would like to put these quotes over one of the pictures attached; Instagram (new size: 4:5 (1080 x 1350 pixels) One Quote per picture, and I want the quote to be bold or easy to read as well. I provided a few reference graphics that I really like as examples below. In very small letters at the bottom add @KimBarlowDaily

All of the pictures are attached; you can pick any photo and add one quote to it; but no stock photography

```html
<!DOCTYPE html>
<html lang="en">
<head>
<meta charset="utf-8">
<title>Quote Cards With KB – May 2025</title>
<link rel="stylesheet" href="https://fonts.googleapis.com/css2?family=Lora:wght@500;600&family=Montserrat:wght@500&display=swap">
<style>
  :root {
    --page: #ffffff;
    --pink: #e8318c;
    --pink-deep: #d81f7c;
    --pink-soft: #f25aa6;
    --white: #ffffff;
    --frame: rgba(255,255,255,0.9);
  }
  * { box-sizing: border-box; margin: 0; padding: 0; }
  html, body {
    width: 1200px; height: 3112px; overflow: hidden;
    background: var(--page);
  }
  .sheet {
    position: relative; width: 1200px; height: 3112px;
    display: grid;
    grid-template-columns: 468px 468px;
    grid-auto-rows: 585px;
    column-gap: 52px;
    row-gap: 30px;
    padding: 33px 106px;
  }
  .card {
    position: relative; overflow: hidden;
    background: linear-gradient(160deg, var(--pink-soft), var(--pink) 45%, var(--pink-deep));
  }
  .card__photo {
    position: absolute; left: 0; top: 0; bottom: 0; width: 60%;
  }
  .card__photo::after {
    content: ""; position: absolute; inset: 0;
    background: linear-gradient(90deg, rgba(232,49,140,0) 50%, var(--pink) 100%);
  }
  .tone-grey  { background: linear-gradient(180deg, #c9c2c4, #8a7d80 55%, #5a4a4d); }
  .tone-light { background: linear-gradient(180deg, #e9e4e2, #b9a9a6 55%, #3b2e2f); }
  .tone-warm  { background: linear-gradient(180deg, #d98a3f, #b86b8c 50%, #c4569a); }
  .tone-dark  { background: linear-gradient(180deg, #d6cfcc, #6d5a57 50%, #2a2224); }
  .tone-sun   { background: linear-gradient(180deg, #b7c4d6, #d9a24a 45%, #b58a86); }
  .tone-room  { background: linear-gradient(180deg, #e3ddd6, #8b6f60 50%, #3a2a25); }
  .card__frame {
    position: absolute; inset: 20px;
    border: 2px solid var(--frame); border-radius: 22px;
  }
  .card__quote {
    position: absolute; left: 51%; right: 28px; top: 17%;
    font-family: "Lora", Georgia, serif; font-weight: 500;
    font-size: 26px; line-height: 1.2; color: var(--white);
    text-align: center;
  }
  .card__quote p + p { margin-top: 20px; }
  .card__handle {
    position: absolute; left: 42px; bottom: 36px;
    font-family: "Montserrat", Arial, sans-serif; font-weight: 500;
    font-size: 12px; color: var(--white);
  }
</style>
</head>
<body>
<main class="sheet">

  <article class="card">
    <div class="card__photo tone-grey" role="img" aria-label="Photo of the host in a pale outfit, seen from behind"></div>
    <div class="card__frame"></div>
    <div class="card__quote">
      <p>The stubborn belly fat after 40? It's not about calories; it's about your hormones.</p>
      <p>Here is the fix!</p>
    </div>
    <span class="card__handle">@KimBarlowDaily</span>
  </article>

  <article class="card">
    <div class="card__photo tone-light" role="img" aria-label="Photo of the host standing in a black outfit"></div>
    <div class="card__frame"></div>
    <div class="card__quote">
      <p>What worked in your 30s won't work now. Here's what actually does.</p>
      <p>Drop 30 pound in 3 Months.</p>
    </div>
    <span class="card__handle">@KimBarlowDaily</span>
  </article>

  <article class="card">
    <div class="card__photo tone-warm" role="img" aria-label="Photo of the host in a pink dress in a warm-lit room"></div>
    <div class="card__frame"></div>
    <div class="card__quote">
      <p>Tired. Moody. Stubborn Belly Fat. Your hormones are screaming for help!</p>
      <p>Let's Fix that.</p>
    </div>
    <span class="card__handle">@KimBarlowDaily</span>
  </article>

  <article class="card">
    <div class="card__photo tone-dark" role="img" aria-label="Photo of the host in a black sheer top and trousers"></div>
    <div class="card__frame"></div>
    <div class="card__quote">
      <p>You're doing all the "right" things, but your belly won't go down?</p>
      <p>Here's what you haven't tried.</p>
    </div>
    <span class="card__handle">@KimBarlowDaily</span>
  </article>

  <article class="card">
    <div class="card__photo tone-sun" role="img" aria-label="Photo of the host in a mauve outfit beside sunflowers"></div>
    <div class="card__frame"></div>
    <div class="card__quote">
      <p>That stubborn weight? It's not your fault... Your hormones are to blame and you're not alone:</p>
      <p>But there is fix.</p>
    </div>
    <span class="card__handle">@KimBarlowDaily</span>
  </article>

  <article class="card">
    <div class="card__photo tone-dark" role="img" aria-label="Photo of the host posing in a black sheer outfit"></div>
    <div class="card__frame"></div>
    <div class="card__quote">
      <p>This 90-day plan helped women over 40 slim down, get a tiny waist and feel sexy again.</p>
      <p>You're next.</p>
    </div>
    <span class="card__handle">@KimBarlowDaily</span>
  </article>

  <article class="card">
    <div class="card__photo tone-room" role="img" aria-label="Photo of the host in a beige top indoors"></div>
    <div class="card__frame"></div>
    <div class="card__quote">
      <p>Your belly isn't fat... it's hormonal. And here's how to fix it.</p>
      <p>Comment HORMONES ifnothing is working.</p>
    </div>
    <span class="card__handle">@KimBarlowDaily</span>
  </article>

  <article class="card">
    <div class="card__photo tone-light" role="img" aria-label="Photo of the host in a black outfit outdoors"></div>
    <div class="card__frame"></div>
    <div class="card__quote">
      <p>This is the secret women over 40 are using to get snatched; without starving.</p>
      <p>Comment SKINNYto get the exact plan.</p>
    </div>
    <span class="card__handle">@KimBarlowDaily</span>
  </article>

  <article class="card">
    <div class="card__photo tone-room" role="img" aria-label="Photo of the host in a fitted black outfit indoors"></div>
    <div class="card__frame"></div>
    <div class="card__quote">
      <p>Falt tummy in your 40s? It's still possible!</p>
      <p>Comment BYE BELLY to get the 10 secrets to flatter tummy</p>
    </div>
    <span class="card__handle">@KimBarlowDaily</span>
  </article>

  <article class="card">
    <div class="card__photo tone-grey" role="img" aria-label="Photo of the host in a black outfit against a light wall"></div>
    <div class="card__frame"></div>
    <div class="card__quote">
      <p>Bloating. Muffin top. Puffy waistline. Your body's screaming for adifferent kind of fix.</p>
      <p>Here it is</p>
    </div>
    <span class="card__handle">@KimBarlowDaily</span>
  </article>

</main>
</body>
</html>
```